Candle Labels for 9 oz tumbler soy candles

Looking for new label design for my candle business. Currently, using a label I designed that needs to be more professional rather than looking homemade. Wanting a professional, clean looking label that enhances my product line. My candle tumblers are white and at times I also use tin containers for my candles so wanting something that will provide a modern/elegant feel to them

Industry/Entity Type

Business

Font styles to use
Decorative
Script

Colors

Designer to choose colors to be used in the design.

Requirements
Must have
• My logo, net weight 9 oz, Space for the name of the Candle (one example is Velvet Dunes
• Looking for something sleek and clean looking, no clutter
Nice to have
• website url www.amberhollowwick.shopnest.com, words "Soy Candle" on the label

```html
<!DOCTYPE html>
<html lang="en">
<head>
<meta charset="utf-8">
<title>Velvet Dunes Soy Candle Label</title>
<link rel="stylesheet" href="https://fonts.googleapis.com/css2?family=Yesteryear&family=Josefin+Sans:wght@700&family=Roboto:wght@400;500&display=swap">
<style>
  :root {
    --pine: #3f5f55;
    --amber: #f6a93b;
    --paper: #ffffff;
  }
  html, body {
    margin: 0;
    padding: 0;
    width: 1200px;
    height: 922px;
    overflow: hidden;
    background: var(--paper);
  }
  .label {
    display: block;
    width: 1200px;
    height: 922px;
  }
  .label__ring-outer { fill: var(--paper); stroke: var(--pine); stroke-width: 4; }
  .label__ring-inner { fill: none; stroke: var(--amber); stroke-width: 3; }
  .label__brand {
    font-family: "Roboto", sans-serif;
    font-weight: 400;
    font-size: 44px;
    fill: var(--pine);
  }
  .label__brand-dot { fill: var(--amber); }
  .label__scent {
    font-family: "Yesteryear", cursive;
    font-size: 118px;
    fill: var(--pine);
  }
  .label__ribbon { fill: var(--amber); }
  .label__type {
    font-family: "Josefin Sans", sans-serif;
    font-weight: 700;
    font-size: 44px;
    letter-spacing: 1px;
    fill: var(--pine);
  }
  .label__url {
    font-family: "Roboto", sans-serif;
    font-weight: 500;
    font-size: 25px;
    fill: var(--pine);
  }
  .label__weight {
    font-family: "Roboto", sans-serif;
    font-weight: 400;
    font-size: 32px;
    fill: var(--amber);
  }
</style>
</head>
<body>
<svg class="label" viewBox="0 0 1200 922" xmlns="http://www.w3.org/2000/svg">
  <circle class="label__ring-outer" cx="600" cy="461" r="350"/>
  <circle class="label__ring-inner" cx="600" cy="461" r="336"/>

  <g class="label__brand-lockup">
    <circle class="label__brand-dot" cx="364" cy="309" r="9"/>
    <text class="label__brand" x="388" y="324" text-anchor="start" textLength="456" lengthAdjust="spacingAndGlyphs">Amber Hollow Wick Co.</text>
  </g>

  <text class="label__scent" x="600" y="482" text-anchor="middle">Velvet Dunes</text>

  <polygon class="label__ribbon" points="343,542 857,542 825,572 857,603 343,603 375,572"/>
  <text class="label__type" x="600" y="590" text-anchor="middle">SOY CANDLE</text>

  <text class="label__url" x="600" y="657" text-anchor="middle">www.amberhollowwick.shopnest.com</text>
  <text class="label__weight" x="600" y="732" text-anchor="middle">Net weight 9 oz</text>
</svg>
</body>
</html>
```